Educational clinic needs a new webpage design

I have a relatively new website but I am unhappy with the design. I was hoping the look of it would more match my logo, brochures, business cards, and postcards. The content is good and it's already mobile ready. The designer used square space, which I would like to keep if possible. My website is www.willowgatestudio.com

Target Market(s)

Parents of school age children

Industry/Entity Type

Education

Number of Pages Required

5+ page

Requirements
Must have
• Pictures must depict the diversity of our students. We service all ages, from preschool through college and our students come from varying races.
Should not have
• I try to avoid the word "tutoring" because what we do is so much more. I like the tag line of "results that go beyond traditional tutoring"

```html
<!DOCTYPE html>
<html lang="en">
<head>
<meta charset="utf-8">
<title>Willowgate Learning Studio</title>
<link rel="stylesheet" href="https://fonts.googleapis.com/css2?family=Josefin+Sans:wght@400;600;700&family=Open+Sans:wght@400;600;700&display=swap">
<style>
:root{
  --purple:#5b2a84;
  --purple-dark:#4a1f6d;
  --purple-mid:#6a3594;
  --green:#8cc63f;
  --green-dark:#74a92e;
  --ink:#444;
  --muted:#777;
  --light:#f3f3f5;
  --white:#fff;
  --red:#d0282e;
}
*{box-sizing:border-box;margin:0;padding:0}
html,body{width:1200px;height:3600px;overflow:hidden}
body{font-family:"Open Sans",Arial,sans-serif;color:var(--ink);background:var(--white);position:relative}
.heading{font-family:"Josefin Sans","Trebuchet MS",sans-serif}
section,header,footer{position:absolute;left:0;width:1200px}

/* header */
.site-header{top:0;height:90px;background:var(--white);border-bottom:1px solid #e5e5e5}
.topbar{height:22px;border-bottom:1px solid #eee;display:flex;align-items:center;padding:0 60px;font-size:11px;color:var(--muted)}
.topbar .social{display:flex;gap:8px;margin-right:14px}
.topbar .social span{width:10px;height:10px;background:#888;display:block}
.topbar .promo{margin-left:auto;color:var(--red)}
.navrow{display:flex;align-items:center;height:68px;padding:0 60px}
.brand{display:flex;align-items:center;gap:10px;font-family:"Josefin Sans",sans-serif;font-weight:700;font-size:19px;color:var(--purple)}
.brand i{width:34px;height:34px;border-radius:50%;background:var(--purple);display:block}
.nav{margin-left:auto;display:flex;gap:28px;align-items:center;font-size:13px;color:#333}
.nav .cta{background:#333a4a;color:#fff;padding:9px 14px;border-radius:3px}

/* hero */
.hero{top:90px;height:410px;background:#f7f7f7}
.hero-photo{position:absolute;left:0;top:0;width:720px;height:410px;background:linear-gradient(135deg,#5f8a6a 0%,#3f6b55 45%,#c9a98a 100%)}
.hero-copy{position:absolute;left:755px;top:70px;color:var(--purple)}
.hero-copy .big{font-size:104px;font-weight:700;color:var(--green);line-height:1}
.hero-copy .line1{font-size:50px;line-height:1.1;margin-top:8px}
.hero-copy .line2{font-size:40px;line-height:1.1}
.btn-green{display:inline-block;background:var(--green);color:#fff;font-weight:700;border-radius:3px}
.hero-copy .btn-green{margin-top:38px;font-family:"Josefin Sans",sans-serif;font-size:20px;padding:20px 18px;box-shadow:0 3px 0 var(--green-dark)}

/* stats */
.stats{top:500px;height:112px;display:flex}
.stat{width:240px;height:112px;color:#fff;display:flex;flex-direction:column;align-items:center;justify-content:center;background:var(--purple)}
.stat:nth-child(even){background:var(--purple-mid)}
.stat .num{font-family:"Josefin Sans",sans-serif;font-size:40px;display:flex;align-items:center;gap:8px}
.stat .lbl{font-size:14px;color:#e4d6f0;margin-top:2px}
.stat svg{width:32px;height:32px;fill:#fff}

/* welcome */
.welcome{top:612px;height:468px;text-align:center;background:var(--white)}
.welcome .sub{margin-top:62px;font-size:25px;color:#555}
.welcome h1{font-size:40px;font-weight:400;color:var(--green);margin-top:4px;letter-spacing:1px}
.divider{width:400px;height:1px;background:#ccc;margin:22px auto;position:relative}
.divider::after{content:"";position:absolute;left:198px;top:-3px;width:6px;height:6px;background:var(--purple);border-radius:50%}
.welcome p{width:800px;margin:36px auto 0;font-size:15px;line-height:25px;color:#777}
.welcome .actions{margin-top:50px;display:flex;justify-content:center;gap:60px}
.welcome .btn-green{font-size:12px;padding:9px 16px;font-weight:400}

/* help */
.help{top:1080px;height:648px;background:var(--purple)}
.help-copy{position:absolute;left:52px;top:56px;width:520px;color:#fff}
.help-copy h2{font-size:44px;font-weight:400}
.help-copy p{font-size:13.5px;line-height:21px;margin-top:26px}
.help-copy h3{font-size:14px;font-weight:700;margin-top:18px;text-transform:uppercase}
.help-copy ul{margin-top:10px;padding-left:22px;font-size:13.5px;line-height:26.8px}
.help-photo{position:absolute;left:586px;top:0;width:614px;height:648px;background:linear-gradient(120deg,#dde3e8 0%,#c7d3da 40%,#8fc06a 75%,#e07a9a 100%)}

/* programs */
.programs{top:1728px;height:572px;background:var(--light);text-align:center}
.programs .ask{margin-top:62px;font-size:23px;color:#555}
.programs .phone{font-size:46px;color:var(--green);font-weight:400;margin-top:6px;letter-spacing:1px}
.cols{display:flex;gap:50px;padding:0 58px;margin-top:48px;text-align:left}
.col{width:328px}
.col h4{font-family:"Josefin Sans",sans-serif;font-size:18px;color:#333;font-weight:600;display:flex;gap:10px;align-items:center;letter-spacing:1px}
.col h4 svg{width:18px;height:18px;fill:var(--green)}
.col p{font-size:13px;line-height:19.6px;color:#666;margin-top:12px}
.col .btn-green{font-size:12px;padding:5px 12px;font-weight:400;margin-top:14px;margin-left:100px}

/* reviews */
.reviews{top:2300px;height:868px;background:var(--purple)}
.reviews h2{text-align:center;color:#fff;font-size:28px;font-weight:400;margin-top:60px;letter-spacing:1px}
.review-grid{display:grid;grid-template-columns:repeat(3,230px);column-gap:100px;row-gap:58px;margin:60px 0 0 155px}
.review{color:#fff;position:relative}
.review .date{font-size:10px;font-style:italic;color:#d9c9e8}
.review .stars{color:#f2c230;font-size:12px;letter-spacing:1px;margin-top:4px}
.review .quote{font-size:15px;line-height:21px;margin-top:4px;padding-left:10px;position:relative}
.review .quote::before{content:"\201C";position:absolute;left:-14px;top:-12px;font-size:58px;color:#7d55a0;font-family:Georgia,serif}
.review .more{font-size:11px;color:var(--green);padding-left:10px}
.review .name{font-size:11px;font-style:italic;text-align:right;margin-top:12px;color:#e8dcf3}
.quicklinks{display:flex;justify-content:space-between;padding:0 90px;margin-top:110px}
.quick{width:110px;text-align:center;color:#fff;font-size:13px}
.quick .ring{width:96px;height:96px;border:3px solid #fff;border-radius:50%;margin:0 auto 14px;display:flex;align-items:center;justify-content:center}
.quick svg{width:40px;height:40px;fill:#fff}

/* footer */
.site-footer{top:3168px;height:432px;background:var(--light)}
.foot-left{position:absolute;left:62px;top:40px;width:320px}
.foot-title{font-size:14px;font-weight:700;color:#444;text-transform:uppercase;letter-spacing:.5px}
.tags{display:flex;flex-wrap:wrap;gap:6px;margin-top:12px}
.tags span{border:1px solid #ccc;font-size:10px;padding:4px 7px;background:#fff;color:#555}
.social-box{margin-top:12px;width:312px;height:200px;border:4px solid var(--green);background:#fff;position:relative}
.social-box .cover{height:88px;background:linear-gradient(90deg,#2f4f2f,#5a7d3a)}
.social-box .cname{position:absolute;left:60px;top:10px;color:#fff;font-size:13px;font-weight:700}
.social-box .like{position:absolute;left:8px;top:96px;background:#4a6aa5;color:#fff;font-size:10px;padding:3px 8px}
.social-box .friends{position:absolute;left:8px;top:150px;font-size:10px;color:#777}
.foot-center{position:absolute;left:410px;top:40px;width:380px;text-align:center}
.foot-mark{width:240px;height:270px;margin:20px auto 0;display:flex;flex-direction:column;align-items:center;justify-content:center;gap:14px}
.foot-mark i{width:120px;height:120px;border-radius:50%;background:var(--purple);display:block}
.foot-mark b{font-family:"Josefin Sans",sans-serif;font-size:22px;color:var(--purple)}
.copyright{font-size:11px;color:#777;margin-top:12px;line-height:16px}
.foot-right{position:absolute;left:822px;top:40px;width:330px}
.news{margin-top:12px}
.news-item{display:flex;gap:10px;margin-bottom:12px}
.news-item i{width:34px;height:34px;background:#7fa64a;display:block;flex:none}
.news-item b{font-size:12px;color:#333;display:block}
.news-item small{font-size:10px;color:#888}
.contact-row{display:flex;gap:10px;margin-top:16px;font-size:12px;line-height:17px;color:#444}
.contact-row svg{width:26px;height:26px;fill:var(--green);flex:none}
</style>
</head>
<body>

<header class="site-header">
  <div class="topbar">
    <div class="social"><span></span><span></span><span></span><span></span></div>
    <span>Cell: 555-014-2290</span>
    <span class="promo">HURRY! Early bird discount $20 – Reserve your seat 2 month before! Register Now</span>
  </div>
  <div class="navrow">
    <div class="brand"><i></i>Willowgate Learning Studio</div>
    <nav class="nav"><span>Home</span><span>Services</span><span>About Us</span><span>Online Payment</span><span>Blog</span><span class="cta">Contact Us</span></nav>
  </div>
</header>

<section class="hero">
  <div class="hero-photo" role="img" aria-label="Photo of a diverse group of smiling school children in front of a classroom chalkboard"></div>
  <div class="hero-copy heading">
    <div class="big">RESULTS</div>
    <div class="line1">that Go Beyond</div>
    <div class="line2">Traditional Tutoring</div>
    <span class="btn-green">GET FREE CONSULTATION</span>
  </div>
</section>

<section class="stats">
  <div class="stat"><div class="num"><svg viewBox="0 0 24 24"><path d="M2 10h4v12H2zM8 22V10l5-8c2 0 3 1 2.5 3L14 9h6c1.5 0 2.5 1.3 2 2.8l-2.5 8.5c-.4 1-1.2 1.7-2.3 1.7z"/></svg>100%</div><div class="lbl">Quality Training</div></div>
  <div class="stat"><div class="num"><svg viewBox="0 0 24 24"><path d="M5 2h14v2h-1c0 4-3 6-4 8 1 2 4 4 4 8h1v2H5v-2h1c0-4 3-6 4-8-1-2-4-4-4-8H5zm3 2c0 3 3 5 4 7 1-2 4-4 4-7z"/></svg>24</div><div class="lbl">Years of experience</div></div>
  <div class="stat"><div class="num"><svg viewBox="0 0 24 24"><circle cx="12" cy="7" r="5"/><path d="M2 23c0-6 4-9 10-9s10 3 10 9z"/></svg>9</div><div class="lbl">Expert Teachers</div></div>
  <div class="stat"><div class="num"><svg viewBox="0 0 24 24"><path d="M12 1l3.4 7 7.6 1-5.5 5.3 1.3 7.7L12 18.3 5.2 22l1.3-7.7L1 9l7.6-1z"/></svg>15</div><div class="lbl">Courses</div></div>
  <div class="stat"><div class="num"><svg viewBox="0 0 24 24"><circle cx="8" cy="7" r="4"/><circle cx="17" cy="8" r="3"/><path d="M0 22c0-5 3-8 8-8s8 3 8 8zM15 13c5 0 9 2 9 7h-6c0-3-1-5-3-7z"/></svg>480+</div><div class="lbl">Members</div></div>
</section>

<section class="welcome">
  <div class="sub heading">Results that go beyond traditional tutoring</div>
  <h1 class="heading">WELCOME TO WILLOWGATE LEARNING STUDIO</h1>
  <div class="divider"></div>
  <p>Willowgate Learning Studio has been helping families with their educational needs for more than 10 years. We are more than passionate about students' success. At Willowgate you'll find a welcoming environment, kind smiles and highly trained Learning Skills Specialists. Students will find a place where they will always be successful!</p>
  <div class="actions"><span class="btn-green">▣ Check Services</span><span class="btn-green">▣ Apply Now</span></div>
</section>

<section class="help">
  <div class="help-copy">
    <h2 class="heading">How We Can Help?</h2>
    <p>At Willowgate Learning Studio our primary goal is to find out the underlying cause of why a student may not be doing well in school. We don't want to put a bandage on the problem; we want to eliminate the problem. Our job is to make sure children are successful learners.</p>
    <h3>We can help all kinds of minds including:</h3>
    <ul>
      <li>Anxiety Problems</li><li>Attention Deficit Hyperactivity Disorder</li><li>Auditory Processing Issues</li><li>Language Processing Issues</li><li>Autism Spectrum Disorders</li><li>Developmental Delays</li><li>Dyslexia</li><li>Executive Function Weakness</li><li>Learning Disabilities</li><li>Memory Weaknesses</li><li>Sensory Integration Disorders</li><li>Language problems</li>
    </ul>
  </div>
  <div class="help-photo" role="img" aria-label="Photo of smiling students holding colourful folders"></div>
</section>

<section class="programs">
  <div class="ask heading">What programs would best suit your child's needs?</div>
  <div class="phone heading">FREE CONSULTATION - (555) 014-2290</div>
  <div class="cols">
    <div class="col">
      <h4><svg viewBox="0 0 24 24"><path d="M12 1l3.4 7 7.6 1-5.5 5.3 1.3 7.7L12 18.3 5.2 22l1.3-7.7L1 9l7.6-1z"/></svg>BRISK</h4>
      <p>The BRISK program is a cognitive brain training program based on proven ideas from the fields of behavioral optometry and cognitive neuroscience. It consists of a number of brain exercises designed to improve mental processing speed, working memory, attention, sequential processing, spatial orientation, visual and auditory memory, phonological awareness, motor planning, problem solving, and reasoning. All the work is done one-on-one with a clinician.</p>
      <span class="btn-green">▣ Read More</span>
    </div>
    <div class="col">
      <h4><svg viewBox="0 0 24 24"><path d="M12 1l3.4 7 7.6 1-5.5 5.3 1.3 7.7L12 18.3 5.2 22l1.3-7.7L1 9l7.6-1z"/></svg>FLUENT PATH READING PROGRAM</h4>
      <p>The Fluent Path Reading Program is designed to promote reading accuracy (decoding) and spelling (encoding) skills for students with word-level deficits. The program is designed to teach phonemic awareness, alphabetic principles (sound-symbol relationship), word study, spelling, sight word instruction, fluency, vocabulary, oral expressive language development, and comprehension. For more information, visit their website online here.</p>
      <span class="btn-green">▣ Read More</span>
    </div>
    <div class="col">
      <h4><svg viewBox="0 0 24 24"><path d="M12 1l3.4 7 7.6 1-5.5 5.3 1.3 7.7L12 18.3 5.2 22l1.3-7.7L1 9l7.6-1z"/></svg>NEUROFEEDBACK</h4>
      <p>This is a therapy technique that presents the user with real-time feedback on brainwave activity. Brainwave activity is measured by sensors on the scalp, typically in the form of a video display, sound or vibration. The aim is to provide real-time information to the Central Nervous System (CNS) as to its current activity. For more information, visit their website online here. (We have a licensed therapist who can bill insurance.)</p>
      <span class="btn-green">▣ Read More</span>
    </div>
  </div>
</section>

<section class="reviews">
  <h2 class="heading">WHAT OTHERS SAY ABOUT US</h2>
  <div class="review-grid">
    <div class="review"><div class="date">Friday, June 3, 2016</div><div class="stars">★★★★★</div><div class="quote">Our son reads with real confidence now, and homework nights are calm again. Thank you all...</div><div class="more">Read More</div><div class="name">- Mara Lindqvist</div></div>
    <div class="review"><div class="date">Thursday, June 2, 2016</div><div class="stars">★★★★★</div><div class="quote">The staff found the root of the struggle in weeks, not years. We saw progress right away...</div><div class="more">Read More</div><div class="name">- Dana Holloway</div></div>
    <div class="review"><div class="date">Thursday, June 2, 2016</div><div class="stars">★★★★★</div><div class="quote">A warm place with kind, skilled people. My daughter looks forward to every single session...</div><div class="more">Read More</div><div class="name">- Priya Okafor</div></div>
    <div class="review"><div class="date">Wednesday, June 1, 2016</div><div class="stars">★★★★★</div><div class="quote">Focus and memory both improved, and his teachers noticed the change before we told them...</div><div class="more">Read More</div><div class="name">- Tomas Reyna</div></div>
    <div class="review"><div class="date">Sunday, May 29, 2016</div><div class="stars">★★★★★</div><div class="quote">Clear plans, honest updates and real results. We recommend them to every family we know...</div><div class="more">Read More</div><div class="name">- Lena Marsh</div></div>
    <div class="review"><div class="date">Wednesday, May 25, 2016</div><div class="stars">★★★★★</div><div class="quote">They treat each child as a whole person. Our college student finally enjoys learning again...</div><div class="more">Read More</div><div class="name">- Owen Castell</div></div>
  </div>
  <div class="quicklinks">
    <div class="quick"><div class="ring"><svg viewBox="0 0 24 24"><path d="M2 10h4v12H2zM8 22V10l5-8c2 0 3 1 2.5 3L14 9h6c1.5 0 2.5 1.3 2 2.8l-2.5 8.5c-.4 1-1.2 1.7-2.3 1.7z"/></svg></div>MORE REVIEWS</div>
    <div class="quick"><div class="ring"><svg viewBox="0 0 24 24"><path d="M2 5h20v14H2zm2 2v2h16V7zm0 5v5h16v-5zm2 2h6v2H6z"/></svg></div>PAYMENT PAGE</div>
    <div class="quick"><div class="ring"><svg viewBox="0 0 24 24"><path d="M3 4h3v3H3zm5 0h13v3H8zM3 10h3v3H3zm5 0h13v3H8zM3 16h3v3H3zm5 0h13v3H8z"/></svg></div>EXAM PREP</div>
    <div class="quick"><div class="ring"><svg viewBox="0 0 24 24"><circle cx="12" cy="7" r="5"/><path d="M2 23c0-6 4-9 10-9s10 3 10 9z"/></svg></div>OUR STAFF</div>
    <div class="quick"><div class="ring"><svg viewBox="0 0 24 24"><path d="M21 2C12 3 6 9 4 18l-2 4h2l2-4c5 0 9-3 10-7h-4l5-2c2-2 3-4 4-7z"/></svg></div>CONTACT US</div>
  </div>
</section>

<footer class="site-footer">
  <div class="foot-left">
    <div class="foot-title">Important Links</div>
    <div class="tags"><span>Resources</span><span>How We Can Help?</span><span>Summer Sessions</span><span>Online Payment Page</span><span>What We Do?</span><span>Contact Us</span></div>
    <div class="foot-title" style="margin-top:30px">Find us on Socialbook</div>
    <div class="social-box">
      <div class="cover" role="img" aria-label="Cover photo of the studio page"></div>
      <div class="cname">Willowgate Learning Studio</div>
      <div class="like">Like Page</div>
      <div class="friends">Be the first of your friends to like this</div>
    </div>
  </div>
  <div class="foot-center">
    <div class="foot-mark"><i></i><b>Willowgate Learning Studio</b></div>
    <div class="copyright">© Copyright 2016 · Willowgate Learning Studio</div>
  </div>
  <div class="foot-right">
    <div class="foot-title">Latest News / Blogs</div>
    <div class="news">
      <div class="news-item"><i></i><div><b>How to Reduce your stress?</b><small>July 9, 2016 - 7:58 am</small></div></div>
      <div class="news-item"><i></i><div><b>Our summer expert learning classes</b><small>May 1, 2016 - 6:51 am</small></div></div>
    </div>
    <div class="foot-title" style="margin-top:18px">Find us here!</div>
    <div class="contact-row"><svg viewBox="0 0 24 24"><path d="M12 1a8 8 0 0 0-8 8c0 6 8 14 8 14s8-8 8-14a8 8 0 0 0-8-8zm0 11a3 3 0 1 1 0-6 3 3 0 0 1 0 6z"/></svg><div><b>Address :</b> WILLOWGATE LEARNING STUDIO,<br>418 ALDER ROW, BROOKFIELD, OR, 97201</div></div>
    <div class="contact-row"><svg viewBox="0 0 24 24"><path d="M2 5h20v14H2zm2 2v.5l8 5 8-5V7z"/></svg><div><b>Email :</b><br>INFO@WILLOWGATESTUDIO.COM</div></div>
    <div class="contact-row"><svg viewBox="0 0 24 24"><path d="M6.6 10.8a15 15 0 0 0 6.6 6.6l2.2-2.2c.3-.3.7-.4 1-.2 1.1.4 2.3.6 3.6.6.6 0 1 .4 1 1V20c0 .6-.4 1-1 1A17 17 0 0 1 3 4c0-.6.4-1 1-1h3.5c.6 0 1 .4 1 1 0 1.3.2 2.5.6 3.6.1.3 0 .7-.2 1z"/></svg><div><b>Phone :</b> 555-014-2290</div></div>
  </div>
</footer>

</body>
</html>
```